Vorbel Neutraceuticals Needs a New Label Design!

Vorbel is a neutraceutical line of vitamins, supplements and protein powders. We are looking for a new look/feel for our labels to really make them pop off the shelf.

Some brands we like are:
www.pemsy.com
www.kelvorida.com
www.dubrin.com

We are going to have square bottles and caps that will most likely be white or clear. We'd like a look/feel that uses bold colors and perhaps foil to make the design stand out.

The labels may be different colors for each product, but the general look/feel should be the same. To learn more about Vorbel, take a look at www.qtremedics.com/vorbel.

We are also reformulating to make our products natural, organic and non-GMO. A look gearing more towards a holistic feel might work!

We have a logo that we cannot change, but we are not committed to the colors of it (Orange and green) and it does NOT have to be prominent on the label itself.

Design must utilize our icons (see website and attached files)

Vorbels tagline is: Shaping Strong Lives
Updates

Project Deadline Extended
Reason: We wanted to extend this project to give designers a bit more time to work on it!

Target Market(s)

Women and Men who are serious about their health, women purchasing vitamins for family....

Industry/Entity Type

Health And Wellness

Font styles to use
Decorative

Requirements
Must have
• Must:
• -Utilize our icons
• -Have bold colors
• -Stand out on a shelf
Nice to have
• The "Bel" in "Vorbel" should stand out

```html
<!DOCTYPE html>
<html lang="en">
<head>
<meta charset="utf-8">
<title>Vorbel Super B Complex Label</title>
<link href="https://fonts.googleapis.com/css2?family=Raleway:wght@300;400;500&family=Lato:ital,wght@0,700;0,900;1,400&display=swap" rel="stylesheet">
<style>
  :root {
    --page-bg: #ececec;
    --label-bg: #dcedf5;
    --seal-blue: #1b6fbf;
    --badge-blue: #22a3de;
    --white: #ffffff;
    --navy: #0d2e5c;
    --icon-red: #e0262b;
    --icon-sky: #2ea6dc;
    --icon-brown: #9a6b45;
    --icon-yellow: #f3d21c;
    --icon-purple: #8a2a87;
    --icon-teal: #1f9a8a;
  }
  * { box-sizing: border-box; margin: 0; padding: 0; }
  html, body { width: 1200px; height: 849px; overflow: hidden; }
  body { background: var(--page-bg); position: relative; font-family: 'Lato', sans-serif; }

  .label {
    position: absolute; left: 300px; top: 24px;
    width: 600px; height: 800px;
    background: var(--label-bg);
  }
  .seal-ring { position: absolute; left: 14px; top: 114px; width: 572px; height: 572px; }
  .seal {
    position: absolute; left: 20px; top: 120px;
    width: 560px; height: 560px; border-radius: 50%;
    background: var(--seal-blue); overflow: hidden;
    color: var(--white); text-align: center;
  }
  .brand {
    position: absolute; top: 46px; left: 0; right: 0;
    display: flex; justify-content: center; align-items: center; gap: 12px;
  }
  .brand-dot { width: 26px; height: 26px; border-radius: 50%; background: var(--white); }
  .brand-name { font-family: 'Raleway', sans-serif; font-weight: 300; font-size: 44px; color: var(--white); }
  .brand-rule { position: absolute; top: 106px; left: 150px; width: 260px; height: 1px; background: rgba(255,255,255,.6); }

  .product-name {
    position: absolute; top: 116px; left: 0; right: 0;
    font-family: 'Raleway', sans-serif; font-weight: 400; line-height: 1;
  }
  .product-name .line-1 { display: block; font-size: 78px; }
  .product-name .line-2 { display: block; font-size: 86px; margin-top: 4px; }

  .category {
    position: absolute; top: 292px; left: 30px; right: 30px;
    display: flex; align-items: center; gap: 14px;
    font-family: 'Raleway', sans-serif; font-weight: 500; font-size: 17px; letter-spacing: .5px;
  }
  .category::before, .category::after { content: ""; flex: 1; height: 2px; background: rgba(255,255,255,.85); }

  .benefit-icons {
    position: absolute; top: 326px; left: 0; right: 0;
    display: flex; justify-content: center; gap: 10px;
  }
  .benefit-icon {
    width: 56px; height: 56px; border-radius: 50%;
    border: 2px solid var(--white);
    display: flex; align-items: center; justify-content: center;
  }
  .icon-heart { background: var(--icon-red); }
  .icon-brain { background: var(--icon-sky); }
  .icon-hair { background: var(--icon-brown); }
  .icon-eye { background: var(--icon-yellow); }
  .icon-pills { background: var(--icon-purple); }
  .icon-joint { background: var(--icon-teal); }

  .claim {
    position: absolute; top: 396px; left: 0; right: 0;
    font-style: italic; font-size: 17px; line-height: 1.3;
  }

  .count-badge {
    position: absolute; left: 190px; top: 462px;
    width: 180px; height: 140px; border-radius: 50%;
    background: var(--badge-blue); color: var(--navy);
    padding-top: 12px;
  }
  .count-badge .count { display: block; font-weight: 900; font-size: 44px; line-height: 1; color: var(--white); }
  .count-badge .unit { display: block; font-weight: 700; font-size: 16px; line-height: 1.1; }
  .count-badge .supply { display: block; font-weight: 400; font-size: 11px; }
</style>
</head>
<body>
  <main class="label">
    <svg class="seal-ring" viewBox="0 0 572 572" aria-hidden="true">
      <defs>
        <linearGradient id="silver" x1="0" y1="0" x2="1" y2="1">
          <stop offset="0" stop-color="#f4f4f4"/>
          <stop offset=".35" stop-color="#9a9a9a"/>
          <stop offset=".6" stop-color="#ffffff"/>
          <stop offset="1" stop-color="#7c7c7c"/>
        </linearGradient>
      </defs>
      <circle cx="286" cy="286" r="284" fill="url(#silver)"/>
    </svg>

    <section class="seal">
      <div class="brand">
        <span class="brand-dot"></span>
        <span class="brand-name">Vorbel</span>
      </div>
      <div class="brand-rule"></div>

      <h1 class="product-name">
        <span class="line-1">SUPER B</span>
        <span class="line-2">COMPLEX</span>
      </h1>

      <p class="category">DIETARY SUPPLEMENT</p>

      <div class="benefit-icons">
        <span class="benefit-icon icon-heart" role="img" aria-label="Heart health">
          <svg width="30" height="28" viewBox="0 0 30 28"><path d="M15 26 C4 18 1 12 1 8 A7 7 0 0 1 15 5 A7 7 0 0 1 29 8 C29 12 26 18 15 26Z" fill="#fff"/></svg>
        </span>
        <span class="benefit-icon icon-brain" role="img" aria-label="Brain health"></span>
        <span class="benefit-icon icon-hair" role="img" aria-label="Hair health"></span>
        <span class="benefit-icon icon-eye" role="img" aria-label="Eye health">
          <svg width="34" height="20" viewBox="0 0 34 20"><path d="M1 10 Q17 -6 33 10 Q17 26 1 10Z" fill="#fff"/><circle cx="17" cy="10" r="5" fill="#8a6a10"/></svg>
        </span>
        <span class="benefit-icon icon-pills" role="img" aria-label="Blood cell health"></span>
        <span class="benefit-icon icon-joint" role="img" aria-label="Joint health"></span>
      </div>

      <p class="claim">Excellent source of Omega 3 fatty acids<br>and Vitamins A, E &amp; D</p>

      <div class="count-badge">
        <span class="count">180</span>
        <span class="unit">Capsules</span>
        <span class="supply">30 Day Supply</span>
      </div>
    </section>
  </main>
</body>
</html>
```